Brovemo / stay-brightened -> Align your thoughts and emotions with world peace

[En español at the end] Very good! Thank you for showing interest in our project :) We need a logo design and web design for a foundation based in Barcelona. Our goal is to work with people's psychology and philosophy to make their lives happier as well as the rest of the world, because we believe we can align them. The name of the foundation is "brovemo" (brovémo), which comes to say that there is a way to align a series of concepts that take us from the peace and inner happiness of the individual to world peace and happiness. Very much in the line of Tomas Verlinde's quotation: "All the problems of humanity derive from that we do not know how to remain alone and quiet in a room". The concepts we want to align are the following, and in this order: Inner Peace Practical Philosophy Emotional Intelligence Critical Thinking Social Justice Conflict Resolution World Peace We enclose a couple of possible logo and web ideas, very grotesque and rudimentary. We are sure that you will be able to capture the idea and improve it in such a way that the idea will win with your contribution. Thank you very much in advance! Ah! And, brovemo :-) -------------- Hi! Thanks for paying attention to this project! We are looking for a logo and web design for an association whose goal is to work with the psychology and philosophy of people in order to make their life happier as well as the happiness of the rest of the world. The name of the organization is "brovemo" (get aligned) meaning that we can align ourselves with the next concepts (in this order): inner peace - practical philosophy - emotional intelligence - critical thinking - social justice - conflict resolution - global Peace Find some basic ideas that you might find in order to grasp what we are looking for, but feel free to add your own contribution, I am sure you can surprise us! :) Thank you in advance, Get aligned!

Target Market(s)

We addressed mainly middle-class people with concerns for personal development. In the medium term, we plan to cover the spectrum of companies with training courses for their staff. The first project that we are sure will be carried out is the application of critical thinking for adolescents and young people.

Logo Text

Brove-m

Number of Pages Required

1 page

Font styles to use
Sans Serif

Colors
3176b5
f37122

Requirements
Must have
• The essential elements are relatively abstract and numerous. Those exposed before: Inner Peace, Practical Philosophy, Emotional Intelligence, Critical Thinking, Social Justice, Conflict Resolution, World Peace. Probably the most striking or relevant will be two: emotional intelligence and critical thinking. The next level would be occupied by inner peace through meditation and introspection. And in the last level the other three.
Nice to have
• We want to transmit integrity and transparency, which in turn will be pillars of the educational and philosophical methods that we will teach. Empathy and compassion are also key. We have marked some colors, but still feel free to use another / others in your design. Sure you have great ideas :-) and we are looking forward to seeing them
Should not have
• We want to avoid at all costs the sensation of pseudoscience and volatility. Our values ​​are deep and we prefer to die rather than transmit an ambiguous, wrong, superfluous or interested message (in the sense of chaquetero).

```html
<!DOCTYPE html>
<html lang="es">
<head>
<meta charset="utf-8">
<title>Brovemo</title>
<link rel="stylesheet" href="https://fonts.googleapis.com/css2?family=Open+Sans:ital,wght@0,400;0,600;0,700;1,400&family=Oswald:wght@500;600&display=swap">
<style>
:root{
  --brand:#3176b5;
  --accent:#f37122;
  --white:#ffffff;
  --ink:#333333;
  --footer:#1c1c1c;
  --footer-text:#9a9a9a;
  --line:rgba(255,255,255,.55);
}
*{box-sizing:border-box;margin:0;padding:0}
html,body{width:1200px;height:4180px;overflow:hidden}
body{font-family:"Open Sans",Arial,sans-serif;color:var(--white);background:var(--white);position:relative}

.site-header{height:100px;background:var(--white);display:flex;align-items:center;position:relative}
.brand{position:absolute;left:238px;top:24px;display:flex;align-items:center;gap:12px}
.brand-dot{width:52px;height:52px;border-radius:50%;background:var(--brand)}
.brand-name{font-family:"Open Sans",Arial,sans-serif;font-weight:600;font-size:40px;color:var(--brand);letter-spacing:.5px}
.main-nav{position:absolute;left:690px;top:42px;display:flex;gap:34px}
.main-nav a{font-size:12px;color:#666;text-decoration:none}

.hero{position:relative;height:292px;background:linear-gradient(100deg,#51684f 0%,#6f8160 22%,#2f3d3a 55%,#1f2d45 80%,#3c5a7a 100%);overflow:hidden}
.hero-title{position:absolute;top:12px;width:100%;text-align:center;font-family:"Oswald",Arial,sans-serif;font-weight:500;font-size:27px;letter-spacing:3px}
.hero-main{position:absolute;left:180px;top:144px;width:206px;height:206px;margin-top:-103px;border-radius:50%;background:var(--white);border:6px solid rgba(255,255,255,.5);box-shadow:0 0 0 8px rgba(255,255,255,.25);display:flex;align-items:center;justify-content:center;text-align:center;color:#3a3a3a;font-family:"Oswald",Arial,sans-serif;font-weight:600;font-size:40px;line-height:1.05}
.hero-step{position:absolute;top:214px;width:96px;height:96px;margin:-48px 0 0 -48px;border-radius:50%;border:2px solid rgba(255,255,255,.8);display:flex;align-items:center;justify-content:center;text-align:center;font-size:12px;line-height:1.2;padding:8px;text-transform:uppercase}
.hero-lines{position:absolute;inset:0}

.topic{position:relative;height:500px;text-align:center;padding:26px 270px 0}
.topic-bg{position:absolute;inset:0}
.topic-inner{position:relative}
.topic h2{font-size:32px;font-weight:700;margin-bottom:8px;text-shadow:0 1px 4px rgba(0,0,0,.5)}
.topic .lead{font-size:11px;font-style:italic;line-height:1.4;margin:0 40px 38px;text-shadow:0 1px 2px rgba(0,0,0,.6)}
.topic p{font-size:12.5px;font-style:italic;line-height:1.45;margin-bottom:22px;text-shadow:0 1px 3px rgba(0,0,0,.7)}

.t1 .topic-bg{background:linear-gradient(180deg,#7b8a9a 0%,#5c6670 40%,#3f3a32 100%)}
.t2 .topic-bg{background:linear-gradient(180deg,#a98a5c 0%,#b26b2e 50%,#4a3426 100%)}
.t3 .topic-bg{background:linear-gradient(180deg,#b8a27a 0%,#8b7a60 45%,#3c3a36 100%)}
.t4 .topic-bg{background:radial-gradient(circle at 50% 50%,#3b4c3f 0%,#27362c 60%,#18221b 100%)}
.t5 .topic-bg{background:linear-gradient(90deg,#5e2e1e 0%,#6a4228 20%,#3c6a3a 45%,#2f5a8a 70%,#6a3a6a 100%)}
.t6 .topic-bg{background:linear-gradient(180deg,#b9b5b0 0%,#9c918a 50%,#7a6d64 100%)}
.t7 .topic-bg{background:linear-gradient(180deg,#5e9a3a 0%,#3d7a26 50%,#275a18 100%)}

.guide{position:absolute;left:0;top:0;width:1200px;height:4180px;pointer-events:none}

.site-footer{position:relative;height:284px;background:var(--footer);text-align:center;padding-top:52px}
.footer-brand{display:inline-flex;align-items:center;gap:12px}
.footer-brand .brand-dot{width:54px;height:54px}
.footer-brand .brand-name{font-size:42px}
.footer-nav{margin-top:22px;display:flex;justify-content:center;gap:28px}
.footer-nav a{font-size:11px;color:var(--footer-text);text-decoration:none}
.social{margin-top:40px;display:flex;justify-content:center;gap:28px}
.social span{width:26px;height:26px;border-radius:50%;background:var(--brand);display:block}
.footer-rule{position:absolute;bottom:12px;left:580px;width:40px;height:2px;background:#555}
</style>
</head>
<body>

<header class="site-header">
  <div class="brand"><span class="brand-dot"></span><span class="brand-name">brovemo</span></div>
  <nav class="main-nav"><a>Inicio</a><a>Filosofía</a><a>participar</a><a>contacto</a></nav>
</header>

<section class="hero" role="img" aria-label="Paisaje de bosque a la izquierda y globo terrestre nocturno a la derecha">
  <svg class="hero-lines" width="1200" height="292" viewBox="0 0 1200 292">
    <line x1="180" y1="144" x2="1000" y2="214" stroke="rgba(255,255,255,.5)" stroke-width="1.5"/>
    <circle cx="180" cy="144" r="150" fill="none" stroke="rgba(255,255,255,.25)"/>
    <circle cx="978" cy="214" r="80" fill="none" stroke="rgba(255,255,255,.35)"/>
    <line x1="978" y1="262" x2="978" y2="292" stroke="rgba(255,255,255,.55)"/>
  </svg>
  <h1 class="hero-title">BROVEMO-TU PAZ INTERIOR Y LA MUNDIAL</h1>
  <div class="hero-main">PAZ<br>INTERIOR</div>
  <div class="hero-step" style="left:442px">Filosofía práctica</div>
  <div class="hero-step" style="left:550px">Inteligencia emocional</div>
  <div class="hero-step" style="left:655px">Pensamiento crítico</div>
  <div class="hero-step" style="left:763px">Resolución conflictos</div>
  <div class="hero-step" style="left:876px">Justicia social</div>
  <div class="hero-step" style="left:981px">Paz mundial</div>
</section>

<section class="topic t1"><div class="topic-bg" role="img" aria-label="Persona meditando sobre rocas ante un cielo abierto"></div><div class="topic-inner">
<h2>Paz interior</h2>
<p class="lead">Cras a fringilla ipsum, vel tempus mauris. Sed dictum erat eros, vel tincidunt lectus maximus eu. Morbi sem orci, ultricies vitae efficitur eu, suscipit ac neque. Lorem ipsum dolor sit amet, consectetur adipiscing elit.</p>
<p>Fusce semper velit non neque auctor ultricies. Praesent ullamcorper ipsum nec nisl pellentesque tristique. Nunc commodo metus eu dolor viverra, quis semper magna accumsan. Nulla vitae nisl eu quam accumsan feugiat. In laoreet tortor neque, eget fringilla orci rutrum in. Suspendisse bibendum convallis dui, in bibendum nibh consequat eu. Nulla vestibulum ex vel sit amet hendrerit. Fusce id turpis id nibh dignissim dictum. Proin sed magna tincidunt, porttitor velit vitae, maximus eros. Phasellus tincidunt pretium nunc at amet lobortis. Integer a ipsum vitae est consequat convallis nec nec turpis.</p>
<p>Etiam bibendum quam vel eros ornare scelerisque. Sed quis tortor pulvinar, maximus metus sed, porttitor tortor. Praesent imperdiet, ex et malesuada scelerisque, eros purus fermentum nisi, nec porta magna tortor ut lacus. Suspendisse eget viverra mi. Aliquam erat volutpat. Nunc a suscipit magna, vitae lacinia metus. Interdum et malesuada fames ac ante ipsum primis in faucibus. Cras ultrices consectetur lectus, a dignissim justo luctus sed. Nullam lacinia mollis diam eget tristique.</p>
</div></section>

<section class="topic t2"><div class="topic-bg" role="img" aria-label="Vía de tren hacia el atardecer"></div><div class="topic-inner">
<h2>Filosofía Práctica</h2>
<p class="lead">Cras a fringilla ipsum, vel tempus mauris. Sed dictum erat eros, vel tincidunt lectus maximus eu. Morbi sem orci, ultricies vitae efficitur eu, suscipit ac neque. Lorem ipsum dolor sit amet, consectetur adipiscing elit.</p>
<p>Fusce semper velit non neque auctor ultricies. Praesent ullamcorper ipsum nec nisl pellentesque tristique. Nunc commodo metus eu dolor viverra, quis semper magna accumsan. Nulla vitae nisl eu quam accumsan feugiat. In laoreet tortor neque, eget fringilla orci rutrum in. Suspendisse bibendum convallis dui, in bibendum nibh consequat eu. Nulla vestibulum ex vel sit amet hendrerit. Fusce id turpis id nibh dignissim dictum. Proin sed magna tincidunt, porttitor velit vitae, maximus eros. Phasellus tincidunt pretium nunc at amet lobortis. Integer a ipsum vitae est consequat convallis nec nec turpis.</p>
<p>Etiam bibendum quam vel eros ornare scelerisque. Sed quis tortor pulvinar, maximus metus sed, porttitor tortor. Praesent imperdiet, ex et malesuada scelerisque, eros purus fermentum nisi, nec porta magna tortor ut lacus. Suspendisse eget viverra mi. Aliquam erat volutpat. Nunc a suscipit magna, vitae lacinia metus. Interdum et malesuada fames ac ante ipsum primis in faucibus. Cras ultrices consectetur lectus, a dignissim justo luctus sed. Nullam lacinia mollis diam eget tristique.</p>
</div></section>

<section class="topic t3"><div class="topic-bg" role="img" aria-label="Figura pensativa bajo una nube de colores sobre una mesa"></div><div class="topic-inner">
<h2>Inteligencia emocional</h2>
<p class="lead">Cras a fringilla ipsum, vel tempus mauris. Sed dictum erat eros, vel tincidunt lectus maximus eu. Morbi sem orci, ultricies vitae efficitur eu, suscipit ac neque. Lorem ipsum dolor sit amet, consectetur adipiscing elit.</p>
<p>Fusce semper velit non neque auctor ultricies. Praesent ullamcorper ipsum nec nisl pellentesque tristique. Nunc commodo metus eu dolor viverra, quis semper magna accumsan. Nulla vitae nisl eu quam accumsan feugiat. In laoreet tortor neque, eget fringilla orci rutrum in. Suspendisse bibendum convallis dui, in bibendum nibh consequat eu. Nulla vestibulum ex vel sit amet hendrerit. Fusce id turpis id nibh dignissim dictum. Proin sed magna tincidunt, porttitor velit vitae, maximus eros. Phasellus tincidunt pretium nunc at amet lobortis. Integer a ipsum vitae est consequat convallis nec nec turpis.</p>
<p>Etiam bibendum quam vel eros ornare scelerisque. Sed quis tortor pulvinar, maximus metus sed, porttitor tortor. Praesent imperdiet, ex et malesuada scelerisque, eros purus fermentum nisi, nec porta magna tortor ut lacus. Suspendisse eget viverra mi. Aliquam erat volutpat. Nunc a suscipit magna, vitae lacinia metus. Interdum et malesuada fames ac ante ipsum primis in faucibus. Cras ultrices consectetur lectus, a dignissim justo luctus sed. Nullam lacinia mollis diam eget tristique.</p>
</div></section>

<section class="topic t4"><div class="topic-bg" role="img" aria-label="Laberinto circular en tonos verdes oscuros"></div><div class="topic-inner">
<h2>Pensamiento crítico</h2>
<p class="lead">Cras a fringilla ipsum, vel tempus mauris. Sed dictum erat eros, vel tincidunt lectus maximus eu. Morbi sem orci, ultricies vitae efficitur eu, suscipit ac neque. Lorem ipsum dolor sit amet, consectetur adipiscing elit.</p>
<p>Fusce semper velit non neque auctor ultricies. Praesent ullamcorper ipsum nec nisl pellentesque tristique. Nunc commodo metus eu dolor viverra, quis semper magna accumsan. Nulla vitae nisl eu quam accumsan feugiat. In laoreet tortor neque, eget fringilla orci rutrum in. Suspendisse bibendum convallis dui, in bibendum nibh consequat eu. Nulla vestibulum ex vel sit amet hendrerit. Fusce id turpis id nibh dignissim dictum. Proin sed magna tincidunt, porttitor velit vitae, maximus eros. Phasellus tincidunt pretium nunc at amet lobortis. Integer a ipsum vitae est consequat convallis nec nec turpis.</p>
<p>Etiam bibendum quam vel eros ornare scelerisque. Sed quis tortor pulvinar, maximus metus sed, porttitor tortor. Praesent imperdiet, ex et malesuada scelerisque, eros purus fermentum nisi, nec porta magna tortor ut lacus. Suspendisse eget viverra mi. Aliquam erat volutpat. Nunc a suscipit magna, vitae lacinia metus. Interdum et malesuada fames ac ante ipsum primis in faucibus. Cras ultrices consectetur lectus, a dignissim justo luctus sed. Nullam lacinia mollis diam eget tristique.</p>
</div></section>

<section class="topic t5"><div class="topic-bg" role="img" aria-label="Bolas de papel arrugado de colores sobre madera"></div><div class="topic-inner">
<h2>Resolución conflictos</h2>
<p class="lead">Cras a fringilla ipsum, vel tempus mauris. Sed dictum erat eros, vel tincidunt lectus maximus eu. Morbi sem orci, ultricies vitae efficitur eu, suscipit ac neque. Lorem ipsum dolor sit amet, consectetur adipiscing elit.</p>
<p>Fusce semper velit non neque auctor ultricies. Praesent ullamcorper ipsum nec nisl pellentesque tristique. Nunc commodo metus eu dolor viverra, quis semper magna accumsan. Nulla vitae nisl eu quam accumsan feugiat. In laoreet tortor neque, eget fringilla orci rutrum in. Suspendisse bibendum convallis dui, in bibendum nibh consequat eu. Nulla vestibulum ex vel sit amet hendrerit. Fusce id turpis id nibh dignissim dictum. Proin sed magna tincidunt, porttitor velit vitae, maximus eros. Phasellus tincidunt pretium nunc at amet lobortis. Integer a ipsum vitae est consequat convallis nec nec turpis.</p>
<p>Etiam bibendum quam vel eros ornare scelerisque. Sed quis tortor pulvinar, maximus metus sed, porttitor tortor. Praesent imperdiet, ex et malesuada scelerisque, eros purus fermentum nisi, nec porta magna tortor ut lacus. Suspendisse eget viverra mi. Aliquam erat volutpat. Nunc a suscipit magna, vitae lacinia metus. Interdum et malesuada fames ac ante ipsum primis in faucibus. Cras ultrices consectetur lectus, a dignissim justo luctus sed. Nullam lacinia mollis diam eget tristique.</p>
</div></section>

<section class="topic t6"><div class="topic-bg" role="img" aria-label="Manos levantadas de distintas personas"></div><div class="topic-inner">
<h2>Justicia social</h2>
<p class="lead">Cras a fringilla ipsum, vel tempus mauris. Sed dictum erat eros, vel tincidunt lectus maximus eu. Morbi sem orci, ultricies vitae efficitur eu, suscipit ac neque. Lorem ipsum dolor sit amet, consectetur adipiscing elit.</p>
<p>Fusce semper velit non neque auctor ultricies. Praesent ullamcorper ipsum nec nisl pellentesque tristique. Nunc commodo metus eu dolor viverra, quis semper magna accumsan. Nulla vitae nisl eu quam accumsan feugiat. In laoreet tortor neque, eget fringilla orci rutrum in. Suspendisse bibendum convallis dui, in bibendum nibh consequat eu. Nulla vestibulum ex vel sit amet hendrerit. Fusce id turpis id nibh dignissim dictum. Proin sed magna tincidunt, porttitor velit vitae, maximus eros. Phasellus tincidunt pretium nunc at amet lobortis. Integer a ipsum vitae est consequat convallis nec nec turpis.</p>
<p>Etiam bibendum quam vel eros ornare scelerisque. Sed quis tortor pulvinar, maximus metus sed, porttitor tortor. Praesent imperdiet, ex et malesuada scelerisque, eros purus fermentum nisi, nec porta magna tortor ut lacus. Suspendisse eget viverra mi. Aliquam erat volutpat. Nunc a suscipit magna, vitae lacinia metus. Interdum et malesuada fames ac ante ipsum primis in faucibus. Cras ultrices consectetur lectus, a dignissim justo luctus sed. Nullam lacinia mollis diam eget tristique.</p>
</div></section>

<section class="topic t7"><div class="topic-bg" role="img" aria-label="Manos sosteniendo un globo terrestre entre hojas verdes"></div><div class="topic-inner">
<h2>Paz mundial</h2>
<p class="lead">Cras a fringilla ipsum, vel tempus mauris. Sed dictum erat eros, vel tincidunt lectus maximus eu. Morbi sem orci, ultricies vitae efficitur eu, suscipit ac neque. Lorem ipsum dolor sit amet, consectetur adipiscing elit.</p>
<p>Fusce semper velit non neque auctor ultricies. Praesent ullamcorper ipsum nec nisl pellentesque tristique. Nunc commodo metus eu dolor viverra, quis semper magna accumsan. Nulla vitae nisl eu quam accumsan feugiat. In laoreet tortor neque, eget fringilla orci rutrum in. Suspendisse bibendum convallis dui, in bibendum nibh consequat eu. Nulla vestibulum ex vel sit amet hendrerit. Fusce id turpis id nibh dignissim dictum. Proin sed magna tincidunt, porttitor velit vitae, maximus eros. Phasellus tincidunt pretium nunc at amet lobortis. Integer a ipsum vitae est consequat convallis nec nec turpis.</p>
<p>Etiam bibendum quam vel eros ornare scelerisque. Sed quis tortor pulvinar, maximus metus sed, porttitor tortor. Praesent imperdiet, ex et malesuada scelerisque, eros purus fermentum nisi, nec porta magna tortor ut lacus. Suspendisse eget viverra mi. Aliquam erat volutpat. Nunc a suscipit magna, vitae lacinia metus. Interdum et malesuada fames ac ante ipsum primis in faucibus. Cras ultrices consectetur lectus, a dignissim justo luctus sed. Nullam lacinia mollis diam eget tristique.</p>
</div></section>

<footer class="site-footer">
  <div class="footer-brand"><span class="brand-dot"></span><span class="brand-name">brovemo</span></div>
  <nav class="footer-nav"><a>Inicio</a><a>Filosofía</a><a>participar</a><a>contacto</a></nav>
  <div class="social"><span></span><span></span><span></span><span></span><span></span><span></span></div>
  <div class="footer-rule"></div>
</footer>

<svg class="guide" width="1200" height="4180" viewBox="0 0 1200 4180" aria-hidden="true">
  <line x1="978" y1="392" x2="978" y2="3896" stroke="rgba(255,255,255,.55)" stroke-width="1.5"/>
  <g fill="rgba(0,0,0,.25)" stroke="rgba(255,255,255,.8)" stroke-width="1.5">
    <circle cx="978" cy="372" r="9"/><circle cx="978" cy="880" r="9"/><circle cx="978" cy="1378" r="9"/>
    <circle cx="978" cy="1876" r="9"/><circle cx="978" cy="2374" r="9"/><circle cx="978" cy="2872" r="9"/>
    <circle cx="978" cy="3370" r="9"/><circle cx="978" cy="3868" r="9"/>
  </g>
  <g fill="none" stroke="#fff" stroke-width="1.5">
    <path d="M974 370l4 4 4-4"/><path d="M974 878l4 4 4-4"/><path d="M974 1376l4 4 4-4"/>
    <path d="M974 1874l4 4 4-4"/><path d="M974 2372l4 4 4-4"/><path d="M974 2870l4 4 4-4"/>
    <path d="M974 3368l4 4 4-4"/><path d="M974 3866l4 4 4-4"/>
  </g>
</svg>

</body>
</html>
```